Need a web design for my company which has an existing logo already

Hello,
I am looking for a web designer for my sports and well-being company. I've got a logo already which should be used for the creation. I will need the entire design idea for my word press website (5 -10 pages) .
Please see the attached logo.
My company is a yoga, dance and retreat business, but not only for women. So it shouldn't be girly. I am looking for a neutral design.
I am looking forward to read your proposals. Please show me some samples of similar jobs you have done in the past.
best regards,
Tansy

```html
<!DOCTYPE html>
<html lang="en">
<head>
<meta charset="utf-8">
<title>Corevale Studio</title>
<link href="https://fonts.googleapis.com/css2?family=Lato:ital,wght@0,400;0,700;1,400&family=Lora&family=Parisienne&display=swap" rel="stylesheet">
<style>
:root{
  --ink:#111;
  --text:#6e6e6e;
  --blush:#e3d8d8;
  --sage:#a3b3a3;
  --sage-dark:#8fa08f;
  --white:#fff;
  --star:#b8c2b8;
}
*{box-sizing:border-box;margin:0;padding:0}
html,body{width:1200px;height:3645px;overflow:hidden;background:var(--white)}
body{position:relative;font-family:'Lato',sans-serif;color:var(--text)}
.abs{position:absolute}
.script{font-family:'Parisienne',cursive;color:var(--ink);font-weight:400}

.site-header{left:0;top:0;width:1200px;height:103px;background:var(--ink)}
.brand{left:112px;top:30px;font-size:34px;color:var(--white);letter-spacing:1px;display:flex;align-items:center;gap:10px}
.brand-dot{width:10px;height:10px;border-radius:50%;background:var(--white)}
.main-nav{left:400px;top:48px;display:flex;gap:25px;font-size:13px;color:var(--white)}
.main-nav .active{border-bottom:3px solid var(--white);padding-bottom:6px}
.quote-btn{left:913px;top:33px;width:175px;height:46px;border-radius:23px;background:var(--blush);color:var(--ink);font-weight:700;font-size:13px;display:flex;align-items:center;justify-content:center}

.hero{left:0;top:103px;width:1200px;height:689px;background:linear-gradient(180deg,#cfe4e2 0%,#e6efe7 35%,#bcd7d3 55%,#d6e4df 80%,#fff 100%)}
.hero-title{left:0;top:105px;width:1200px;text-align:center;font-size:62px}
.hero-figure{left:440px;top:180px;width:230px;height:360px;border-radius:110px 110px 40px 40px;background:linear-gradient(180deg,#d9cfc4,#f3f1ed)}

.service{width:295px;height:295px;border-radius:50%;background:var(--blush);text-align:center;padding-top:38px}
.service.featured{background:var(--sage);box-shadow:inset 0 0 0 6px var(--sage),inset 0 0 0 8px #e8eee8}
.service svg{width:92px;height:66px}
.service h3{font-family:Arial,sans-serif;font-weight:400;font-size:22px;color:var(--ink);margin-top:14px}
.service p{font-family:Arial,sans-serif;font-size:13px;line-height:22px;color:#6d6d6d;width:235px;margin:8px auto 0}
.service .go{width:35px;height:35px;border-radius:50%;background:var(--sage);margin:12px auto 0;color:var(--white);font-size:14px;line-height:35px}
.service.featured .go{background:var(--blush)}
.circle-shadow{left:490px;top:928px;width:220px;height:26px;border-radius:50%;background:radial-gradient(ellipse,rgba(0,0,0,.2),rgba(0,0,0,0) 70%)}

.story-photo{left:112px;top:1000px;width:463px;height:373px;background:linear-gradient(135deg,#7a6a55,#b8a478 45%,#8e7aa0 80%,#5a4b3e)}
.section-title{font-size:46px}
.story-title{left:615px;top:990px}
.rule{height:2px;width:76px}
.rule.blush{background:#dcc8c8}
.rule.sage{background:var(--sage)}
.story-rule{left:617px;top:1059px}
.story-text{left:617px;top:1087px;width:470px;font-size:12.6px;line-height:22.4px}
.story-text p+p{margin-top:22px}

.banner{left:0;top:1467px;width:1200px;height:428px;background:linear-gradient(90deg,#f6f1dc 0%,#eae3c4 45%,#c7b39a 70%,#d8cdb2 100%)}
.banner-title{left:112px;top:1520px;font-size:64px;line-height:68px}
.learn-btn{left:112px;top:1783px;width:177px;height:47px;border-radius:24px;background:var(--blush);color:var(--ink);font-weight:700;font-size:12px;display:flex;align-items:center;justify-content:center;gap:4px}

.center-title{left:0;width:1200px;text-align:center}
.review{top:2087px;width:309px;height:187px;background:var(--white);box-shadow:0 2px 10px rgba(0,0,0,.08);padding:24px 20px 0 20px}
.review-name{display:flex;align-items:center;gap:10px;font-weight:700;color:var(--ink);font-size:17px}
.review-name .q{color:#c4c4c4;font-size:28px;font-family:Georgia,serif;line-height:1}
.review-body{font-style:italic;font-size:12px;line-height:26px;margin:4px 0 0 30px}
.review-meta{display:flex;justify-content:space-between;margin:10px 0 0 30px;font-size:12px;color:#555}
.stars{color:var(--star);letter-spacing:1px}
.dots{left:545px;top:2322px;display:flex;gap:10px;align-items:center}
.dots span{width:12px;height:12px;border-radius:50%;background:#d3d3d3}
.dots .on{width:26px;height:26px;background:var(--blush);color:var(--white);font-size:11px;text-align:center;line-height:26px}

.post{top:2527px;width:298px;text-align:center}
.post-photo{height:197px;border-radius:4px}
.post h3{font-family:'Lora',serif;font-weight:400;font-size:20px;line-height:34px;color:#333;margin-top:12px;padding:0 50px}
.post time{display:block;font-family:'Lora',serif;font-size:14px;color:#a9a9a9;margin-top:6px}
.post p{font-size:14px;line-height:26px;margin-top:6px;padding:0 10px}
.post .more{display:block;font-family:'Lora',serif;font-size:14px;color:#a9a9a9;margin-top:14px}
.blog-btn{left:522px;top:2955px;width:156px;height:46px;border-radius:23px;background:var(--sage);color:var(--white);font-family:'Lora',serif;font-size:15px;display:flex;align-items:center;justify-content:center}

.gallery{left:0;top:3096px;width:1200px;height:251px;display:flex}
.gallery div{flex:1}

.foot-brand{left:112px;top:3420px;font-size:34px;color:var(--ink);display:flex;align-items:center;gap:10px}
.foot-brand span{width:10px;height:10px;border-radius:50%;background:var(--ink)}
.copy{left:112px;top:3522px;font-size:11.5px;line-height:19px;color:#555}
.foot-col h4{font-size:13px;font-weight:700;color:#8b7b7b;margin-bottom:6px}
.foot-col{font-size:12.5px;line-height:26px;color:#666}
.sitemap ul{list-style:none;display:grid;grid-template-columns:93px 93px}
.contact-line{display:flex;gap:18px;align-items:center}
.ico{width:12px;display:inline-flex;justify-content:center;color:var(--star)}
.follow li{list-style:none;display:flex;gap:18px;align-items:center;line-height:34px}
.follow .dot{width:10px;height:10px;border-radius:50%;background:var(--star)}
</style>
</head>
<body>

<header class="site-header abs">
  <div class="brand abs"><span class="brand-dot"></span>Corevale</div>
  <nav class="main-nav abs">
    <span class="active">HOME</span><span>OUR STORY</span><span>OUR FOCUS</span><span>REVIEWS</span><span>BLOG</span><span>CONTACT US</span>
  </nav>
  <div class="quote-btn abs">REQUEST A QUOTE</div>
</header>

<section class="hero abs" role="img" aria-label="Person meditating in lotus pose on a wooden pier above a calm sea at sunrise"></section>
<h1 class="hero-title abs script">Welcome To Corevale Studio</h1>
<div class="hero-figure abs" role="img" aria-label="Seated yoga figure with raised hands, seen from behind"></div>

<div class="circle-shadow abs"></div>
<article class="service abs" style="left:157px;top:609px">
  <svg viewBox="0 0 92 66" fill="none" stroke="#222" stroke-width="2.4"><path d="M46 8c10 10 10 30 0 46C36 38 36 18 46 8z"/><path d="M46 54C40 34 28 26 18 22c0 16 10 30 28 32zM46 54c6-20 18-28 28-32 0 16-10 30-28 32z"/><path d="M18 30C8 30 4 32 4 36c6 12 22 18 42 18M74 30c10 0 14 2 14 6-6 12-22 18-42 18"/></svg>
  <h3>YOGA</h3>
  <p>Lorem ipsum dolor sit amet, conse ctetur adipiscing elit, sed do eiusmod tempor incididunt</p>
  <div class="go">›</div>
</article>
<article class="service featured abs" style="left:452px;top:609px">
  <svg viewBox="0 0 92 66" fill="none" stroke="#222" stroke-width="2.4"><circle cx="30" cy="12" r="5"/><circle cx="60" cy="10" r="5"/><path d="M30 18v20l-12 22M30 38l10 20M30 24l30-6 12-10M60 16l-4 22-10 22M56 38l14 20M20 26l10-2"/></svg>
  <h3>DANCE</h3>
  <p>Lorem ipsum dolor sit amet, conse ctetur adipiscing elit, sed do eiusmod tempor incididunt</p>
  <div class="go">›</div>
</article>
<article class="service abs" style="left:747px;top:609px">
  <svg viewBox="0 0 92 66" fill="none" stroke="#222" stroke-width="2.4"><path d="M46 40L30 24a9 9 0 0 1 16-10 9 9 0 0 1 16 10z"/><path d="M36 26h6l3-5 4 9 3-4h6"/><path d="M14 10v24l18 16v12M78 10v24L60 50v12M22 30l12 12M70 30L58 42"/></svg>
  <h3>RETREAT BUSINESS</h3>
  <p>Lorem ipsum dolor sit amet, conse ctetur adipiscing elit, sed do eiusmod tempor incididunt</p>
  <div class="go">›</div>
</article>

<div class="story-photo abs" role="img" aria-label="Group of smiling women carrying yoga mats outdoors"></div>
<h2 class="story-title abs script section-title">Our Story</h2>
<div class="story-rule rule blush abs"></div>
<div class="story-text abs">
  <p>Lorem ipsum dolor sit amet, consectetur adipiscing elit, sed do eiusmod tempor incididunt ut labore et dolore magna aliqua. Ut enim ad minim veniam, quis nostrud exercitation ullamco laboris nisi ut aliquip ex ea commodo consequat. Duis aute irure dolor in reprehenderit in voluptate velit esse cillum dolore eu fugiat nulla pariatur. Excepteur sint occaecat cupidatat non proident, sunt in culpa qui officia deserunt mollit anim id est laborum.</p>
  <p>Lorem ipsum dolor sit amet, consectetur adipiscing elit, sed do eiusmod tempor incididunt ut labore et dolore magna aliqua. Ut enim ad minim veniam, quis nostrud exercitation ullamco laboris nisi ut aliquip ex ea commodo consequat. Duis aute irure dolor in reprehenderit in voluptate velit esse cillum dolore eu fugiat nulla pariatur. Excepteur sint occaecat cupidatat non proident, sunt in culpa qui officia deserunt mollit anim id est laborum.</p>
</div>

<section class="banner abs" role="img" aria-label="Woman and man jogging together outdoors in warm sunlight"></section>
<h2 class="banner-title abs script">We are a sports<br>and well-being<br>company.</h2>
<div class="learn-btn abs">LEARN MORE <svg width="11" height="11" viewBox="0 0 12 12"><circle cx="6" cy="6" r="6" fill="#111"/><path d="M4 6h4M6 4l2 2-2 2" stroke="#fff" stroke-width="1.5" fill="none"/></svg></div>

<h2 class="center-title abs script section-title" style="top:1975px">Testimonials</h2>
<div class="rule blush abs" style="left:562px;top:2040px"></div>

<article class="review abs" style="left:112px">
  <div class="review-name"><span class="q">“</span>Mara Lind</div>
  <p class="review-body">Lorem ipsum dolor sit amet, consec tet ur adipiscing elit, sed do eiusmod tem por incididunt ut labore et</p>
  <div class="review-meta"><span>20 jan 2020 at 8.23</span><span class="stars">★★★★★</span></div>
</article>
<article class="review abs" style="left:445px">
  <div class="review-name"><span class="q">“</span>Mara Lind</div>
  <p class="review-body">Lorem ipsum dolor sit amet, consec tet ur adipiscing elit, sed do eiusmod tem por incididunt ut labore et</p>
  <div class="review-meta"><span>20 jan 2020 at 8.23</span><span class="stars">★★★★★</span></div>
</article>
<article class="review abs" style="left:779px">
  <div class="review-name"><span class="q">“</span>Mara Lind</div>
  <p class="review-body">Lorem ipsum dolor sit amet, consec tet ur adipiscing elit, sed do eiusmod tem por incididunt ut labore et</p>
  <div class="review-meta"><span>20 jan 2020 at 8.23</span><span class="stars">★★★★★</span></div>
</article>
<div class="dots abs"><span></span><span class="on">2</span><span></span><span></span><span></span></div>

<h2 class="center-title abs script section-title" style="top:2425px">Testimonials</h2>
<div class="rule sage abs" style="left:562px;top:2498px"></div>

<article class="post abs" style="left:112px">
  <div class="post-photo" role="img" aria-label="Two runners stretching on a hilltop above clouds at sunset" style="background:linear-gradient(180deg,#e8b590,#c98a7a 55%,#5a4a50)"></div>
  <h3>Lorem ipsum dolor sit amet</h3>
  <time>Jun 17, 2020</time>
  <p>Lorem ipsum dolor sit amet, consectetur adipiscing elit, sed do eiusmod</p>
  <span class="more">READ MORE ⟶</span>
</article>
<article class="post abs" style="left:451px">
  <div class="post-photo" role="img" aria-label="Women meditating together on grass outdoors" style="background:linear-gradient(180deg,#9fae7e,#c4b79a 50%,#8a7a6a)"></div>
  <h3>Lorem ipsum dolor sit amet</h3>
  <time>Jun 12, 2020</time>
  <p>Lorem ipsum dolor sit amet, consectetur adipiscing elit, sed do eiusmod</p>
  <span class="more">READ MORE ⟶</span>
</article>
<article class="post abs" style="left:790px">
  <div class="post-photo" role="img" aria-label="Hands passing a crystal over a table of stones and shells" style="background:linear-gradient(135deg,#8a8680,#d8d2cc 50%,#6b645e)"></div>
  <h3>Lorem ipsum dolor sit amet</h3>
  <time>Jun 10, 2020</time>
  <p>Lorem ipsum dolor sit amet, consectetur adipiscing elit, sed do eiusmod</p>
  <span class="more">READ MORE ⟶</span>
</article>
<div class="blog-btn abs">View more Blog</div>

<section class="gallery abs">
  <div role="img" aria-label="Group of women walking along a country path" style="background:linear-gradient(180deg,#b9aa74,#8f8a5c 60%,#6e6a48)"></div>
  <div role="img" aria-label="Class practising tai chi with raised hands" style="background:linear-gradient(135deg,#7a6352,#e2d8d0 50%,#b28a70)"></div>
  <div role="img" aria-label="Friends jumping against a hazy sunset sky" style="background:linear-gradient(180deg,#bcd0c6,#e9dcbc 55%,#a89a70)"></div>
  <div role="img" aria-label="Runners on a bridge at sunrise" style="background:linear-gradient(135deg,#3c3a40,#c9b8a8 45%,#5a5660)"></div>
</section>

<footer>
  <div class="foot-brand abs"><span></span>Corevale</div>
  <div class="copy abs">Copyright 2021 Corevale<br>All Right Reserved</div>
  <div class="foot-col sitemap abs" style="left:403px;top:3437px">
    <h4>SITE MAP</h4>
    <ul><li>Home</li><li>Reviews</li><li>About Us</li><li>Blog</li><li>Our Focus</li><li>Contact Us</li><li>Gallery</li></ul>
  </div>
  <div class="foot-col abs" style="left:669px;top:3437px">
    <h4>CONTACT INFO</h4>
    <div>123, Lorem ipsum dolor sit amet,<br>consectetur</div>
    <div class="contact-line"><span class="ico"><svg width="11" height="11" viewBox="0 0 12 12"><path d="M2 1l3 1-1 2 4 4 2-1 1 3-2 1C5 11 1 7 1 3z" fill="#b8c2b8"/></svg></span>1-800-555-0142</div>
    <div class="contact-line"><span class="ico"><svg width="12" height="9" viewBox="0 0 12 9"><rect width="12" height="9" fill="#b8c2b8"/><path d="M0 0l6 5 6-5" stroke="#fff" fill="none"/></svg></span>hello@corevale.example</div>
  </div>
  <div class="foot-col follow abs" style="left:995px;top:3437px">
    <h4>FOLLOW US</h4>
    <ul><li><span class="dot"></span>Community</li><li><span class="dot"></span>Updates</li><li><span class="dot"></span>Network</li></ul>
  </div>
</footer>

</body>
</html>
```